Tidewell Oyster-new seafood raw bar restaurant menu

We are a Local Seafood & Raw Bar restaurant that is looking to open in 3 months. I need-Dinner Menu Design, Happy Hour Menu, Cocktail Menu, Brunch Menu, Lunch Menu. I'd like to have you start w/ the dinner menu first then whomever I choose will also do the rest of my menus. The SHELLHOUSE by Kelpcove menu is the direction im going for as far as font organization. Id like you to give us our own personal touch. Ive also provided a mock menu that a local designer started that can't finish due to timing.

Target Market(s)

mid to high end casual seafood restaurant

Industry/Entity Type

restaurant

Font styles to use
Serif
Sans Serif

Colors
0054AA
0677BA
7BADD7
CADEEF
E8F1F8
0094D4
00A9DD
6FCCEA
C7EBF8
E9F6FB
00AB8E
00BBA5
67D7C9
C6EFE9
E9F9F6

Requirements
Must have
• 11" x 14" size

```html
<!DOCTYPE html>
<html lang="en">
<head>
<meta charset="utf-8">
<title>Tidewell Oyster — Dinner Menu</title>
<link href="https://fonts.googleapis.com/css2?family=Lobster&family=Montserrat:ital,wght@0,300;0,400;0,700;1,300&display=swap" rel="stylesheet">
<style>
  :root {
    --red: #c4504f;
    --navy: #263a7a;
    --ink: #141414;
    --muted: #5c5c5c;
    --soft: #7d7d7d;
    --band: #c4e0e8;
    --wave: #dcecf6;
    --sketch: #b9cde6;
    --paper: #ffffff;
    --wash: #f1f2f4;
  }
  * { margin: 0; padding: 0; box-sizing: border-box; }
  html, body { width: 1200px; height: 848px; overflow: hidden; background: var(--paper); }
  .menu {
    position: relative; width: 1200px; height: 848px; overflow: hidden;
    font-family: "Montserrat", Arial, sans-serif; color: var(--ink);
    background:
      radial-gradient(ellipse 220px 160px at 300px 330px, var(--wash), transparent 70%),
      radial-gradient(ellipse 200px 180px at 1000px 400px, var(--wash), transparent 70%),
      var(--paper);
  }
  .raw-band { position: absolute; left: 402px; top: 0; width: 399px; height: 848px; background: var(--band); }
  .wave-band { position: absolute; left: 0; top: 779px; width: 1200px; height: 69px; background: var(--wave); opacity: .8; }
  .frame { position: absolute; left: 26px; top: 23px; width: 1145px; height: 802px; border: 1.5px solid #4a4a4a; pointer-events: none; }
  .divider { position: absolute; top: 84px; height: 686px; border-left: 1.5px dotted var(--navy); }
  .sketch { position: absolute; background: var(--sketch); opacity: .3; border-radius: 50%; }

  .script { position: absolute; font-family: "Lobster", cursive; font-weight: 400; line-height: 1; }
  .script--red { color: var(--red); font-size: 60px; }
  .script--navy { color: var(--navy); font-size: 50px; text-align: center; }

  .item { position: absolute; }
  .item__name { font-weight: 700; font-size: 16px; letter-spacing: .2em; line-height: 1.25; white-space: nowrap; }
  .item__desc { font-weight: 300; font-size: 11px; letter-spacing: .08em; color: var(--muted); line-height: 12.5px; white-space: nowrap; }
  .col-left .item { left: 79px; }
  .col-right .item { left: 847px; }
  .col-right .item__desc { line-height: 18px; }
  .col-raw .item { left: 451px; }
  .rule { position: absolute; height: 0; }
  .rule--red { left: 41px; width: 322px; border-top: 1px dotted var(--red); }
  .rule--blue { left: 441px; width: 322px; border-top: 1px dotted #8fb3cc; }

  .heading-center { position: absolute; font-weight: 700; font-size: 16px; letter-spacing: .2em; white-space: nowrap; transform: translateX(-50%); }
  .option { position: absolute; font-weight: 400; font-size: 15px; letter-spacing: .08em; color: var(--soft); line-height: 13px; }
  .price { position: absolute; font-size: 15px; color: var(--soft); }
  .note { position: absolute; font-style: italic; font-weight: 300; font-size: 15px; letter-spacing: .09em; color: var(--muted); transform: translateX(-50%); white-space: nowrap; }

  .kids { position: absolute; left: 418px; top: 662px; width: 361px; height: 135px; border: 2px solid var(--navy); overflow: hidden; }
  .kids__title { position: absolute; left: 0; width: 100%; top: 12px; font-size: 40px; }
  .kids__list { position: absolute; top: 58px; width: 100%; list-style: none; text-align: center; }
  .kids__list li { font-weight: 700; font-size: 16px; letter-spacing: .2em; line-height: 18.5px; }
</style>
</head>
<body>
<main class="menu">
  <div class="raw-band"></div>
  <div class="wave-band" role="img" aria-label="Decorative wave pattern band along the bottom"></div>

  <div class="sketch" style="left:0;top:50px;width:78px;height:89px" role="img" aria-label="Line sketch of a shrimp"></div>
  <div class="sketch" style="left:282px;top:37px;width:120px;height:125px" role="img" aria-label="Line sketch of a crab"></div>
  <div class="sketch" style="left:763px;top:0;width:165px;height:100px" role="img" aria-label="Line sketch of a shrimp"></div>
  <div class="sketch" style="left:364px;top:415px;width:40px;height:74px" role="img" aria-label="Line sketch of a shrimp"></div>
  <div class="sketch" style="left:1110px;top:334px;width:90px;height:147px" role="img" aria-label="Line sketch of a crab"></div>
  <div class="sketch" style="left:1113px;top:698px;width:87px;height:70px" role="img" aria-label="Line sketch of a shrimp"></div>
  <div class="sketch" style="left:698px;top:790px;width:162px;height:58px" role="img" aria-label="Line sketch of a shrimp"></div>
  <div class="sketch" style="left:26px;top:737px;width:40px;height:47px" role="img" aria-label="Line sketch of a leaf"></div>

  <div class="frame"></div>
  <div class="divider" style="left:393px"></div>
  <div class="divider" style="left:811px"></div>

  <section class="col-left">
    <h2 class="script script--red" style="left:78px;top:116px">Smaller</h2>
    <div class="item" style="top:198px"><p class="item__name">FRIED SHRIMP</p><p class="item__desc">Remoulade</p></div>
    <div class="rule rule--red" style="top:232px"></div>
    <div class="item" style="top:236px"><p class="item__name">MUSSELS</p><p class="item__desc">Local bacon, shallot, garlic, tomato,<br>spicy herb butter</p></div>
    <div class="rule rule--red" style="top:285px"></div>
    <div class="item" style="top:287px"><p class="item__name">ROASTED OYSTERS</p><p class="item__desc">½ dozen, Choice of Rockefeller,<br>Bienville, Tidewell special</p></div>
    <div class="rule rule--red" style="top:335px"></div>
    <div class="item" style="top:338px"><p class="item__name">SHRIMP AND GRITS</p><p class="item__desc">Local andouille, roasted peppers,<br>garlic, shallot, charred tomato</p></div>
    <div class="rule rule--red" style="top:387px"></div>
    <div class="item" style="top:392px"><p class="item__name">CRAB MAC’N CHEESE</p><p class="item__desc">Cheddar, fontina, cotija, local pasta<br>shells</p></div>
    <div class="rule rule--red" style="top:439px"></div>
    <div class="item" style="top:443px"><p class="item__name">SHRIMP REMOULADE</p><p class="item__desc">Avocado, fried green tomato</p></div>
    <div class="rule rule--red" style="top:482px"></div>
    <div class="item" style="top:483px"><p class="item__name">PUMPKIN RISOTTO</p><p class="item__desc">Herbs, dried cherry, local mushrooms</p></div>
    <div class="rule rule--red" style="top:521px"></div>
    <div class="item" style="top:523px"><p class="item__name">CAESER</p><p class="item__desc">Baby gem lettuce, parmesan</p></div>
    <div class="rule rule--red" style="top:563px"></div>
    <div class="item" style="top:568px"><p class="item__name">HOLLOWMERE CRISP<br>GREENS SALAD</p><p class="item__desc" style="line-height:14px">Fig, goat cheese, spiced pepitos, sour<br>cherry vinaigrette</p></div>
    <div class="rule rule--red" style="top:640px"></div>
    <div class="item" style="top:646px"><p class="item__name">CLAM CHOWDER</p><p class="item__desc">New England style</p></div>
    <div class="rule rule--red" style="top:684px"></div>
    <div class="item" style="top:689px"><p class="item__name">BAJA FISH TACOS</p><p class="item__desc">Slaw, cilantro, lime</p></div>
    <div class="rule rule--red" style="top:726px"></div>
    <div class="item" style="top:729px"><p class="item__name">STEAK TACO</p><p class="item__desc" style="line-height:14px">Mojo, dried chili salsa, pickled onion,<br>cotija</p></div>
  </section>

  <section class="col-raw">
    <h2 class="script script--navy" style="left:402px;width:399px;top:110px;line-height:46px">Raw Bar/<br>Chilled Seafood</h2>
    <p class="heading-center" style="left:601px;top:253px">OYSTER CHEF’S PREPARATION</p>
    <div class="rule rule--blue" style="top:273px"></div>
    <p class="heading-center" style="left:616px;top:289px">OYSTER SELECTION</p>
    <p class="option" style="left:463px;top:319px">House</p>
    <p class="option" style="left:547px;top:319px">EastCoast</p>
    <p class="option" style="left:665px;top:319px">Regional</p>
    <p class="price" style="left:477px;top:333px">$</p>
    <p class="price" style="left:575px;top:333px">$</p>
    <p class="price" style="left:698px;top:333px">$</p>
    <p class="note" style="left:596px;top:351px">Accompaniments, top’em</p>
    <p class="heading-center" style="left:611px;top:374px">SEAFOOD TOWER</p>
    <p class="option" style="left:477px;top:401px">Small</p>
    <p class="option" style="left:573px;top:401px">Large</p>
    <p class="option" style="left:655px;top:396px">Build your<br>own</p>
    <p class="price" style="left:491px;top:432px">$</p>
    <p class="price" style="left:590px;top:432px">$</p>
    <p class="price" style="left:693px;top:432px">$</p>
    <div class="rule rule--blue" style="top:456px"></div>
    <div class="item" style="top:470px"><p class="item__name">CEVICHE</p><p class="item__desc">Citrus, fruit, peppers, onion, cilantro</p></div>
    <div class="rule rule--blue" style="top:505px"></div>
    <div class="item" style="top:509px"><p class="item__name">TUNA POKE/CRUDO</p><p class="item__desc">Ponzu, scallions, ginger, avocado sesame</p></div>
    <div class="rule rule--blue" style="top:546px"></div>
    <div class="item" style="top:548px"><p class="item__name">SCALLOP CRUDO</p><p class="item__desc">Lemon, ginger, chives, olive oil, pine nutssesame</p></div>
    <div class="rule rule--blue" style="top:584px"></div>
    <div class="item" style="top:588px"><p class="item__name">PEEL AND EAT SHRIMP</p><p class="item__desc">Remoulade, tartar, cocktail nutssesame</p></div>
    <div class="rule rule--blue" style="top:621px"></div>
    <div class="item" style="top:623px"><p class="item__name">LOCAL FISH CRUDO</p><p class="item__desc">Seasonal accompaniments</p></div>

    <div class="kids">
      <h3 class="script script--navy kids__title">Kids Menu</h3>
      <ul class="kids__list">
        <li>CHICKEN TENDERS</li>
        <li>MAC N CHEESE</li>
        <li>FRIED FISH</li>
        <li>FRIED SHRIMP</li>
      </ul>
    </div>
  </section>

  <section class="col-right">
    <h2 class="script script--red" style="left:846px;top:116px">Signatures</h2>
    <div class="item" style="top:198px"><p class="item__name">CLAM LINGUINI</p><p class="item__desc">Local Pasta. Local Bacon, peppers,<br>butter, herbs</p></div>
    <div class="item" style="top:253px"><p class="item__name">VEGETABLE GNOCCHI</p><p class="item__desc">Squash, shallots, peas, mushroom,<br>basil, parmesan</p></div>
    <div class="item" style="top:308px"><p class="item__name">PAN SEARED SCALLOPS</p><p class="item__desc">Curry, cauliflower, carrots, eggplant,<br>Carolina gold rice</p></div>
    <div class="item" style="top:365px"><p class="item__name">HALIBUT GUMBO</p><p class="item__desc">Shrimp, scallions, okra garnish</p></div>
    <div class="item" style="top:407px"><p class="item__name">GRILLED STEAK</p><p class="item__desc">Roasted rainbow carrots, mashed<br>potatoes, ancho demi, chimichurri</p></div>
    <div class="item" style="top:465px"><p class="item__name">SURF AND TURF FILET</p><p class="item__desc">Asparagus, baby potatoes, bearnaise,<br>demi</p></div>
    <div class="item" style="top:521px"><p class="item__name">CRAB LEGS</p><p class="item__desc">Butter, cocktail, spicy remoulade<br>Fresh Catch</p></div>
    <div class="item" style="top:577px"><p class="item__name">LOWCOUNTRY BOIL</p><p class="item__desc">Shrimp, sausage, corn, potato</p></div>
    <div class="item" style="top:618px"><p class="item__name">SMASH BURGER</p><p class="item__desc">Spicy “thousand Island”, pickles, house<br>cut fries, LTO</p></div>
    <div class="item" style="top:671px"><p class="item__name">LOBSTER ROLL</p><p class="item__desc">Lots of Lobstah, scallions, celery, house<br>fries</p></div>
    <div class="item" style="top:723px"><p class="item__name">FISH SANDWICH</p><p class="item__desc">Double stacked halibut, pickled<br>carrots, Lemon/caper/dill aioli, lettuce,</p></div>
  </section>
</main>
</body>
</html>
```